" Somos uma DISTRIBUIDORA DE ALIMENTOS de todos os gêneros. E também temos plantas de BENEFICIAMENTO de produtos para Agricultura Familiar. Nossa linha de produtos de distribuição é bem extensa. Desde pós para gelatina, refrescos, caldos até leite de coco, produtos desidratados, cereais, aveia, panificados (bolos, pães, cookies), fermentos, aromas para indústria de alimentos, etc. Enfim, alimentos e ingredientes no geral sem uma linha específica. Para beneficiamento, trabalhamos atualmente com mix de frutas in natura e bolos regionais (banana, macaxeira, milho, etc). Trabalhamos bem forte na excelência de prestação de serviços e não somente preço de combate. Principalmente por trabalharmos com fábricas de renome no mercado. "

```html
<!DOCTYPE html>
<html lang="pt-BR">
<head>
<meta charset="utf-8">
<title>Assinatura de e-mail — Celeiro72</title>
<link rel="stylesheet" href="https://fonts.googleapis.com/css2?family=Questrial&display=swap">
<style>
  :root {
    --wine: #7a1a36;
    --wine-deep: #6a1530;
    --gold: #c8a15a;
    --paper: #ffffff;
    --backdrop: #e6e6e6;
    --ink-light: #f3e7ea;
  }
  * { margin: 0; padding: 0; box-sizing: border-box; }
  html, body {
    width: 1200px; height: 1200px; overflow: hidden;
    background: var(--backdrop);
    font-family: "Questrial", "Century Gothic", sans-serif;
  }
  .signature {
    position: absolute; left: 100px; top: 482px;
    width: 1000px; height: 236px;
    background: var(--paper);
    border-radius: 6px;
    overflow: hidden;
  }
  .signature__shapes { position: absolute; inset: 0; }
  .monogram {
    position: absolute; left: 22px; top: 18px;
    color: var(--gold); font-size: 34px; letter-spacing: -1px; line-height: 1;
  }
  .contact-row {
    position: absolute; left: 22px;
    display: flex; align-items: center; gap: 26px;
    color: var(--ink-light); font-size: 15px; white-space: nowrap;
  }
  .contact-row--phone { top: 74px; }
  .contact-row--address { top: 109px; }
  .contact-row--web { top: 148px; }
  .contact-item { display: flex; align-items: center; gap: 8px; }
  .contact-icon { width: 18px; height: 18px; flex: none; }
  .brand {
    position: absolute; left: 660px; top: 74px;
    display: flex; align-items: center; gap: 10px;
    color: var(--wine); font-size: 46px; letter-spacing: 0.5px; line-height: 1;
  }
  .brand__dot {
    width: 20px; height: 20px; border-radius: 50%;
    background: var(--gold);
  }
</style>
</head>
<body>
  <div class="signature">
    <svg class="signature__shapes" width="1000" height="236" viewBox="0 0 1000 236">
      <path class="panel" d="M0 14 H500 L550 186 H0 Z" fill="var(--wine)"/>
      <path class="accent-stripe" d="M515 14 H548 L600 186 H567 Z" fill="var(--gold)"/>
      <rect class="bottom-band" x="0" y="186" width="1000" height="12" fill="var(--wine)"/>
      <rect class="gold-rule" x="0" y="203" width="1000" height="6" fill="var(--gold)"/>
      <rect class="wine-rule" x="520" y="213" width="480" height="4" fill="var(--wine-deep)"/>
    </svg>

    <div class="monogram">C72</div>

    <div class="contact-row contact-row--phone">
      <span class="contact-item">
        <svg class="contact-icon" viewBox="0 0 18 18"><circle cx="9" cy="9" r="9" fill="var(--gold)"/><path d="M6 5 L7.5 5 L8.3 7.2 L7.3 8 Q8 10 10 10.7 L10.8 9.7 L13 10.5 L13 12 Q10 13 7.5 10.5 Q5 8 6 5 Z" fill="var(--wine)"/></svg>
        (XX) XXXX.XXX
      </span>
      <span class="contact-item">
        <svg class="contact-icon" viewBox="0 0 18 18"><circle cx="9" cy="9" r="9" fill="var(--gold)"/></svg>
        /celeiro72
      </span>
      <span class="contact-item">
        <svg class="contact-icon" viewBox="0 0 18 18"><circle cx="9" cy="9" r="9" fill="var(--gold)"/></svg>
        @celeiro72
      </span>
    </div>

    <div class="contact-row contact-row--address">
      <span class="contact-item">
        <svg class="contact-icon" viewBox="0 0 18 18"><circle cx="9" cy="9" r="9" fill="var(--gold)"/><path d="M9 3.5 A3.5 3.5 0 0 1 12.5 7 Q12.5 9.5 9 14 Q5.5 9.5 5.5 7 A3.5 3.5 0 0 1 9 3.5 Z" fill="var(--wine)"/><circle cx="9" cy="7" r="1.3" fill="var(--gold)"/></svg>
        Rua das Acácias, 210, Centro - Olinda - PE - CEP 53.120-040
      </span>
    </div>

    <div class="contact-row contact-row--web">
      <span class="contact-item">
        <svg class="contact-icon" viewBox="0 0 18 18"><circle cx="9" cy="9" r="9" fill="var(--gold)"/><circle cx="9" cy="9" r="5" fill="none" stroke="var(--wine)" stroke-width="1.2"/><ellipse cx="9" cy="9" rx="2.2" ry="5" fill="none" stroke="var(--wine)" stroke-width="1.2"/><line x1="4" y1="9" x2="14" y2="9" stroke="var(--wine)" stroke-width="1.2"/></svg>
        www.celeiro72.com.br
      </span>
      <span class="contact-item">
        <svg class="contact-icon" viewBox="0 0 18 18"><circle cx="9" cy="9" r="9" fill="var(--gold)"/><rect x="4" y="5.5" width="10" height="7" fill="var(--wine)"/><path d="M4 5.5 L9 9.5 L14 5.5" fill="none" stroke="var(--gold)" stroke-width="1"/></svg>
        marcos.ribeiro@celeiro72.com.br
      </span>
    </div>

    <div class="brand">
      CELEIRO72
      <span class="brand__dot"></span>
    </div>
  </div>
</body>
</html>
```